Mental Arithmetic Program Brochure

I need a brochure to sell our mental arithmetic program. The brochure will be in two versions:
1. Two page A4 size brochure (front and back)
2. One page A4 size - either a simplified form of the 2-pager or a different thing alltogether

While both will be focused on the same target market, some of the decision makers are housewives and may have more time while others are working and may need a convicing and eye-catching one pager to make a decision.

What I want is 90% decided but I want the designer to be OK with some iterations and modifications at the end to the brochures (2-3 hours of work)

Also, some details like bank account and "contact us" will be put in later so need placeholders for those.

Product is a program of learning mental mathematics through several levels so that children get a very strong foundation of numbes and mathematics and they are able to do amazing mathematical calculations mentally without any pen or paper.

It reduces the dependency on calclators and makes students rely on their brain
It is different because it is a program that will form a strong foundation and build on that to give a holistic learning about numbers and patterns so that children fall in love with numbers and start enjoying it.

In the attached file, I have put some of my thoughts/ points that can be used

If you need any more information about the content etc. or any piece of information you think will be very convincing and need my help to get it, I can try and find that also.

Format must be either in Adobe Illustrator or Adobe InDesign

Target Market(s)

Parents of school going children: late primary to high school (say, 9 to 17 yrs. old)

Also, potentially teachers and adults who can learn it for themselves because they feel they don't have a strong numerical foundation and cannot do mental math.

Requirements
Must have
• Must be very visual. Must be colorful.
• While it is focused on parents, it should make them feel it is just perfect for their children.
• Show the real world benefits of mental mathematics..... How will thiis help their children
• Should show how cheap the cost is in comparison to......some other things
Nice to have
• Benefits of mental math in:
• - life
• - school
• - higher education
• - career
• etc.
Should not have
• Should not be cluttered
• Should not appear very comical or cheesy or cheap... It is serious stuff and it will really benefit their children.... not a gimmicky thing; not a collection of shortcuts; not something offered by anyone out there

```html
<!DOCTYPE html>
<html lang="en">
<head>
<meta charset="utf-8">
<title>Mental Arithmetic Program Brochure</title>
<link href="https://fonts.googleapis.com/css2?family=Crimson+Pro:ital,wght@0,400;0,600;0,700;1,400;1,600;1,700&family=Courier+Prime&display=swap" rel="stylesheet">
<style>
  :root{
    --yellow:#f9ef72;
    --black:#000;
    --ink:#1a1a1a;
    --white:#fff;
    --blue:#29a8e0;
    --red:#d8262e;
    --green:#3ea44a;
  }
  *{box-sizing:border-box;margin:0;padding:0}
  html,body{width:1200px;height:840px;overflow:hidden;background:var(--white)}
  body{position:relative;font-family:"Crimson Pro",Georgia,serif;color:var(--ink)}
  .page{position:absolute;top:53px;width:518px;height:736px;background:var(--white);box-shadow:3px 3px 3px rgba(0,0,0,.45);overflow:hidden}
  .page--front{left:63px}
  .page--back{left:627px}

  .color-band{height:11px;background:linear-gradient(90deg,var(--green),var(--yellow) 20%,var(--blue) 40%,var(--red) 60%,var(--green) 80%,var(--yellow))}

  .kicker{height:26px;background:var(--yellow);text-align:center;font-size:8px;letter-spacing:2.2px;font-weight:600;line-height:28px}
  .challenge{position:relative;height:163px;background:var(--black);color:var(--white)}
  .challenge__title{position:absolute;top:9px;left:0;right:0;text-align:center;font-size:18.5px;font-weight:700;line-height:25px;letter-spacing:.4px}
  .sum{position:absolute;display:block;font-family:"Courier Prime",monospace;font-size:10.5px;line-height:14px;white-space:nowrap}

  .hook{background:var(--yellow);padding:8px 31px 0;height:86px}
  .hook__title{font-size:11px;font-weight:700;line-height:13px;margin-bottom:1px}
  .hook p{font-size:9px;line-height:10.5px}

  .body{padding:14px 30px 0 31px}
  .section{margin-bottom:10px}
  .section__head{font-size:7px;font-weight:700;letter-spacing:.9px;text-transform:uppercase;line-height:10.4px;max-width:400px}
  .body p,.body li{font-size:6.9px;line-height:9.8px}
  .narrow{max-width:405px}
  .bullets{list-style:none;padding-left:8px;max-width:418px}
  .bullets--wide{max-width:445px}
  .bullets li{padding-left:4px;text-indent:-4px}
  .bullets li::before{content:"• "}
  .lead{font-style:italic;font-weight:700}
  .skills{display:grid;grid-template-columns:123px 124px 1fr;padding-left:8px;list-style:none}
  .skills li::before{content:"• "}
  .skills li{font-weight:600}

  .quote{height:60px;background:var(--black);color:var(--white);padding:15px 30px 0 31px;font-style:italic;font-weight:700;font-size:9.7px;line-height:14px;letter-spacing:.3px}
  .back-body{padding:24px 40px 0 31px;height:499px}
  .back-body .section{margin-bottom:10px}
  .back-body p,.back-body li{font-size:6.9px;line-height:12px}
  .back-body .tight p{line-height:9.4px}
  .numbered{padding-left:16px;max-width:400px}
  .numbered li{line-height:9.4px;margin-bottom:3px}
  .strong p{font-weight:700;line-height:9.4px}
  .contact__head{font-size:10px;font-style:italic;font-weight:700;margin-top:4px}
  .contact__line{font-size:5.6px;font-style:italic;white-space:nowrap}

  .cut-line{border-top:1px dashed #999}
  .order{height:166px;background:var(--yellow);padding:14px 34px 0 31px;font-size:7px}
  .order__title{text-align:center;font-size:9px;font-weight:400;letter-spacing:1px;margin-bottom:6px}
  .field-row{display:flex;align-items:flex-end;gap:4px;height:13px}
  .field-row em{font-style:italic}
  .blank{flex:1;border-bottom:.6px solid var(--ink);height:8px}
  .blank--s{flex:0 0 30px}
  .check{display:inline-block;width:6px;height:6px;border:.6px solid var(--ink);margin:0 2px 0 6px;vertical-align:-1px}
  .order__note{font-style:italic;margin-top:8px}
</style>
</head>
<body>

<section class="page page--front">
  <div class="kicker">MENTAL ARITHMETIC PROGRAM</div>
  <div class="challenge">
    <h1 class="challenge__title">How much time would you or your child take<br>to do the following calculations?</h1>
    <span class="sum" style="left:104px;top:68px;transform:rotate(3deg)">1000000 - 987231 = ?</span>
    <span class="sum" style="left:31px;top:91px;transform:rotate(-3deg)">997 x 992 = ?</span>
    <span class="sum" style="left:139px;top:99px">114 x 95= ?</span>
    <span class="sum" style="left:235px;top:76px;transform:rotate(-8deg)">6723673 + 3120982 = ?</span>
    <span class="sum" style="left:413px;top:69px">125^2 = ?</span>
    <span class="sum" style="left:332px;top:97px;transform:rotate(4deg)">Square root of 32041 = ?</span>
    <span class="sum" style="left:31px;top:126px">2 / 29 = ?</span>
    <span class="sum" style="left:107px;top:126px;transform:rotate(2deg)">213827 / 104 = ?</span>
    <span class="sum" style="left:222px;top:117px;transform:rotate(-3deg)">What will be the day of the<br>week on 26th of July 2021?</span>
    <span class="sum" style="left:409px;top:128px">786^2 = ?</span>
  </div>
  <div class="color-band" role="img" aria-label="Band of coloured squares with dots in yellow, blue, red and green"></div>
  <div class="hook">
    <h2 class="hook__title">10 minutes? Maybe 20 minutes? Did you even finish these 10 questions or did you give up?</h2>
    <p>How would you feel if your child could have the skills and the attitude to do all these calculations in less than 7 minutes? The whole list! In 7 minutes or less? How about if they could multiply 102 x 114 (or any other pair three digit numbers) in their head? Without any pen or paper. And add and subtract large numbers mentally. Maybe calculate change at grocery line or in taxi even before the counter clerk or the taxi driver can? IT WILL NEVER HAPPEN: Because our children are learning math the wrong way. They are more likely tolerating math than enjoying it.</p>
  </div>

  <div class="body">
    <div class="section">
      <h3 class="section__head">Do you know that the way of teaching arithmetic calculations in school has not changed in the last 50 years?</h3>
      <p class="narrow">Your kid is probably learning math the same way you did. Now that is not very reassuring. We cannot really expect anyone to learn with the dinosaur method of learning and turn into a genius.</p>
    </div>
    <div class="section">
      <h3 class="section__head">What do we offer?</h3>
      <ul class="bullets">
        <li>A unique and different program to teaching fundamentals of numbers and Math.</li>
        <li>Years of research has helped create this set of exceptional tools, teaching methods, information and insights that help build interest and knowledge about numbers and using arithmetic in life.</li>
        <li>Your kids hate math? They will start loving it. They love math? They will get brilliant at it.</li>
        <li>They will start using numbers in unimaginable ways—EVERYDAY. We make math fun.</li>
        <li>Starting from simple methods, funny stories, delightful outputs and fascinating insights, we develop an interest in Math that children would have never found. They will develop a more natural understanding of numbers and start to enjoy numbers.</li>
      </ul>
    </div>
    <div class="section">
      <h3 class="section__head">Why is math important?</h3>
      <ul class="bullets bullets--wide">
        <li>A great early scientist (often called the Father of Science) said: The book of nature is written in the language of MATHEMATICS.</li>
        <li>Numbers rule our lives. To lead a smart and successful life, mastering numbers is essential.</li>
        <li>From salaries to managing expenses, budgets and bills, credit card charges and other loans, impact of interest rates, to take or not to take a house and mortgage, impact of currency, foreign travel, building savings and growing investments, insurance plans, buying and maintaining cars, children's education etc.</li>
      </ul>
      <p class="lead" style="margin-top:6px">And the sooner you start to master numbers, the more successful you will be. Even more importantly, all gateways to further education, college and graduate entrance exams, test on mathematic reasoning. And while it should be a high scoring section, test takers try to barely pass them or more likely score low because of them. With a good Math foundation in place, scoring high on these tests will be super easy.</p>
    </div>
    <div class="section">
      <h3 class="section__head">How does the program work?</h3>
      <p class="lead">We build on this and teach concepts and mental math techniques that help children gain confidence.</p>
      <p>The “Number Roots” program consists of 7 levels and a total of 50 modules. Each level takes the understanding of and love for numbers to a new level. The “Number Roots” program is a basic course that will show numbers in a new light. It will show aspects of numbers and uses of numbers that will open your eyes.</p>
      <p style="font-style:italic;margin-top:6px">Each module consists of:</p>
      <ul class="bullets">
        <li>Introduction of concepts with full and detailed explanation and examples</li>
        <li>Exercises to practice and reinforce the learning</li>
      </ul>
      <p class="lead" style="margin-top:6px">The full program has more than 1000 exercises and more than 500 pages of learning and practice material.</p>
    </div>
    <div class="section">
      <h3 class="section__head">What are some of the things we teach?</h3>
      <ul class="skills">
        <li>Understanding numbers</li><li>Appreciating numbers</li><li>Mentally adding and subtracting numbers</li>
        <li>Multiplying Numbers</li><li>Adding and Subtracting Time</li><li>Squaring numbers</li>
      </ul>
      <p class="lead" style="margin-top:10px">At the end of 7 modules, every student will get a certificate of completion.<br>The whole program will teach math through games, exercises and insights like nothing you have seen.</p>
    </div>
  </div>
</section>

<section class="page page--back">
  <div class="quote">When children start to understand Math and start doing things that they could not even imagine earlier, they get an improved level of confidence that helps them do better in other subjects also.</div>
  <div class="color-band" role="img" aria-label="Band of coloured squares with dots in yellow, blue, red and green"></div>

  <div class="back-body">
    <div class="section">
      <h3 class="section__head">Cost of the program</h3>
      <p>The full program of 50 modules costs SG$350. As a part of our Singapore launch, we are offering a discounted price of SG$295 (Inclusive of GST).</p>
      <p style="font-style:italic;font-weight:600">Discount of over 15%</p>
      <p>Freebies: This is not all. In the price of this course, we also include:</p>
      <ol class="numbered">
        <li>There are 3 feedback forms in the program. Fill them up completely and send it to get a DVD teaching 25 arithmetic concepts. Worth $150. FREE.</li>
        <li>A free T- Shirt of Count Up company worth $25</li>
        <li>Also, we are organizing four “Mental Math Workshop” in Singapore in Oct-Dec 2009. Students of the program will have a discounted rate of 50%. A saving of $50.</li>
      </ol>
      <div class="tight" style="margin-top:6px"><p>And that's not all. We offer a 100% no-risk guarantee. If you complete the course and feel that despite putting in the required effort you have not learnt anything new, we will return your full program fees. No questions asked.</p></div>
    </div>
    <div class="section">
      <h3 class="section__head">How to order?</h3>
      <p>You can order in 2 ways:</p>
      <ol class="numbered" style="max-width:440px">
        <li>Check Payment: Fill the form at the end of the brochure and mail it with a check of SG$ 295</li>
        <li>Payment on delivery. Email your order at: hello@brightsums.example, with the same details as in the order form.</li>
      </ol>
      <p style="margin-top:6px">We will deliver your order and take cash or check payment on delivery.</p>
    </div>
    <div class="section">
      <h3 class="section__head">Help your child succeed</h3>
      <p>Parents have good intentions and want to help their children get a god education. But you are also hard pressed for time.</p>
      <p>Your choices are limited because everyone has the same way of teaching.</p>
      <p>Doing more of what the school does will not help. Something different is needed.</p>
      <p>Is it very easy? It is not a magic pill. Some effort is needed. But this effort pays off very quickly.</p>
      <p>Is it tough? Not at all. It is a refreshingly different and a brilliant way.</p>
    </div>
    <div class="section tight">
      <h3 class="section__head">Enjoy watching your child succeed.</h3>
      <p>From day 1 you will see an amazing transformation. Within a week you will see your child talking about numbers and impressing you with their grasp of how quickly they are able to do calculations. Within a month you will be shocked at how good their mental calculations are. They will love numbers. They will learn tables of numbers up to 20 in 20 minutes In the 3rd module, they will learn how to multiply numbers like 98 x 92 in less than 10 seconds</p>
    </div>
    <div class="section strong">
      <h3 class="section__head">Do your kid a favor</h3>
      <p>Once your children are shown these techniques, they will excel in all facets of Arithmetic, building a bullet proof foundation for a higher math education. Competition to get into top schools is brutal, give your children the “mental edge” with Number Roots...Order Now!</p>
      <p style="margin-top:9px">In career: Most of the management is about making smart decisions. And that requires being able to master numbers and assess financial impacts of alternative decisions. A good foundation now can help children be smart decision makers tomorrow.</p>
    </div>
    <h3 class="contact__head">Contact Us</h3>
    <p class="contact__line">Bright Sums Academy • 48 Maple Row Eastfield, NW 20418 • (555) 014-2200 • Fax (555) 014-2201 • Account Number: ACC-0000 • Email: hello@brightsums.example</p>
  </div>

  <div class="cut-line"></div>
  <form class="order">
    <h3 class="order__title">ORDER FORM</h3>
    <div class="field-row"><em>Check should be in favour of “</em><span class="blank" style="flex:0 0 175px"></span><em>”</em></div>
    <div class="field-row" style="margin-top:5px">Name <span class="blank"></span> Age <span class="blank blank--s"></span> Email <span class="blank" style="flex:0 0 150px"></span></div>
    <div class="field-row">Parents Name <span class="blank"></span> Email <span class="blank" style="flex:0 0 202px"></span></div>
    <div class="field-row">Contact Number <span class="blank"></span> <em>(R)</em> <span class="blank"></span> <em>(HP)</em></div>
    <div class="field-row">Delivery Address <em>(Please include Pin Code)</em> <span class="blank"></span></div>
    <div class="field-row"><span class="blank"></span></div>
    <div class="field-row" style="margin-top:6px">T-Shirt Size <span class="check"></span>S <span class="check"></span>M <span class="check"></span>L <span class="check"></span>XL</div>
    <p class="order__note">Please mail this form to Bright Sums Academy, 48 Maple Row, Eastfield, NW 20418. Enclosed with check payment of SG $295.</p>
  </form>
</section>

</body>
</html>
```